Turn this into a clear and concise

Attached is a screen shot that we currently show to investors from a software program. We need you to illustrate this in a much more professional looking and easy to view and understand way. If we like your style and attention to detail there is more work behind this.
Industry/Entity Type
Software

```html
<!DOCTYPE html>
<html lang="en">
<head>
<meta charset="utf-8">
<title>Intra-day Countertrend US Hours</title>
<link rel="stylesheet" href="https://fonts.googleapis.com/css2?family=Alegreya+Sans:wght@400;700;800&family=Marcellus&display=swap">
<style>
  :root {
    --page: #dadada;
    --ink: #141414;
    --slate: #4b6275;
    --lime: #8dc63f;
    --shade: #d6dde4;
    --grid: #8a8f94;
    --red-line: #c8202f;
    --orange: #f0a040;
    --navy-dash: #3a5fa0;
    --up: #79b94a;
    --down: #d42a2a;
    --osc: #7cc242;
    --purple: #8a2b8a;
    --ice: #9fd6dc;
    --bar: #1f3a9a;
  }
  * { margin: 0; padding: 0; box-sizing: border-box; }
  html, body { width: 1200px; height: 900px; overflow: hidden; background: var(--page); }
  .canvas { position: relative; width: 1200px; height: 900px; font-family: "Alegreya Sans", sans-serif; color: var(--ink); }
  .title { position: absolute; top: 84px; left: 0; width: 100%; text-align: center; font-weight: 800; font-size: 30px; letter-spacing: .2px; }
  .subtitle { position: absolute; top: 118px; left: 0; width: 100%; text-align: center; font-family: "Marcellus", serif; font-size: 25px; }
  .chart-heading { position: absolute; top: 214px; width: 446px; text-align: center; font-weight: 700; font-size: 20px; letter-spacing: .3px; }
  .chart { position: absolute; top: 267px; width: 446px; height: 446px; }
  .entry { left: 105px; }
  .exit { left: 663px; }
  .axis-label { font-family: "Alegreya Sans", sans-serif; font-weight: 700; font-size: 9px; fill: var(--ink); }
  .axis-label.small { font-size: 4.4px; font-weight: 400; }
  .axis-label.light { fill: #fff; }
  .time-label { font-family: "Alegreya Sans", sans-serif; font-weight: 700; font-size: 9px; fill: var(--ink); }
</style>
</head>
<body>
<div class="canvas">
  <h1 class="title">Intra-day Countertrend US Hours</h1>
  <p class="subtitle">Example Trade: 30 year Treasury Bond, 7/13/14 “Payroll Friday”</p>

  <svg width="0" height="0" style="position:absolute">
    <defs>
      <g id="price-candles">
        <path stroke="#333" stroke-width=".6" d="M12 36V42M19 38V44M26 39V44M33 39V46M40 42V47M47 43V54M54 50V64M61 60V76M68 72V90M75 86V106M82 90V102M89 84V94M96 80V88M103 78V84M110 76V82M117 74V80M124 72V78M131 70V76M138 68V74M145 64V72M152 62V68M159 62V72M166 64V72M173 60V68M180 58V64M187 56V62M194 53V60M201 50V57M208 46V54M215 40V50"/>
        <g fill="var(--down)">
          <rect x="10.5" y="38" width="3" height="2"/><rect x="17.5" y="40" width="3" height="2"/>
          <rect x="31.5" y="41" width="3" height="3"/><rect x="38.5" y="44" width="3" height="1.2"/>
          <rect x="45.5" y="45" width="3" height="7"/><rect x="52.5" y="52" width="3" height="10"/>
          <rect x="59.5" y="62" width="3" height="12"/><rect x="66.5" y="74" width="3" height="14"/>
          <rect x="73.5" y="88" width="3" height="12"/><rect x="157.5" y="64" width="3" height="6"/>
        </g>
        <g fill="var(--up)" stroke="#4c7a2c" stroke-width=".3">
          <rect x="24.5" y="41" width="3" height="1.2"/><rect x="80.5" y="92" width="3" height="8"/>
          <rect x="87.5" y="86" width="3" height="6"/><rect x="94.5" y="82" width="3" height="4"/>
          <rect x="101.5" y="80" width="3" height="2"/><rect x="108.5" y="78" width="3" height="2"/>
          <rect x="115.5" y="76" width="3" height="2"/><rect x="122.5" y="74" width="3" height="2"/>
          <rect x="129.5" y="72" width="3" height="2"/><rect x="136.5" y="70" width="3" height="2"/>
          <rect x="143.5" y="66" width="3" height="4"/><rect x="150.5" y="64" width="3" height="2"/>
          <rect x="164.5" y="66" width="3" height="4"/><rect x="171.5" y="62" width="3" height="4"/>
          <rect x="178.5" y="60" width="3" height="2"/><rect x="185.5" y="58" width="3" height="2"/>
          <rect x="192.5" y="55" width="3" height="3"/><rect x="199.5" y="52" width="3" height="3"/>
          <rect x="206.5" y="48" width="3" height="4"/><rect x="213.5" y="42" width="3" height="6"/>
        </g>
      </g>
      <g id="chart-frame">
        <rect x="0" y="0" width="297" height="297" fill="#fff"/>
        <rect x="52" y="0" width="131" height="120" fill="var(--shade)"/>
        <rect x="227" y="120" width="70" height="157" fill="var(--slate)"/>
        <rect x="0" y="277" width="297" height="20" fill="var(--lime)"/>
        <g stroke="var(--grid)" stroke-width=".6">
          <path d="M0 20H297M0 57H297M0 79H297M0 109H297"/>
          <path d="M40 0V277M100 0V277M157 0V277M213 0V277"/>
        </g>
        <g stroke="var(--ice)" stroke-width=".8">
          <path d="M0 120H297M0 128H227M0 203H227M0 212H297"/>
        </g>
        <path d="M0 140H227" stroke="var(--orange)" stroke-width=".8"/>
        <path d="M0 186H227" stroke="var(--purple)" stroke-width="1"/>
        <path d="M227 0V277" stroke="var(--grid)" stroke-width=".6"/>
        <text class="axis-label" x="234" y="84">136’28</text>
        <text class="axis-label" x="234" y="114">136’16</text>
        <text class="axis-label light" x="234" y="128">100</text>
        <text class="axis-label light" x="234" y="206">0</text>
        <text class="axis-label light" x="234" y="221">20,000</text>
        <text class="axis-label light" x="240" y="244">10,000</text>
        <text class="time-label" x="28" y="291">8am</text>
        <text class="time-label" x="88" y="291">9am</text>
        <text class="time-label" x="143" y="291">10am</text>
        <text class="time-label" x="200" y="291">11am</text>
      </g>
    </defs>
  </svg>

  <div class="chart-heading" style="left:105px">ENTRY (SELL)</div>
  <svg class="chart entry" viewBox="0 0 297 297" role="img" aria-label="Entry (sell) chart: price candles, oscillator and volume">
    <use href="#chart-frame"/>
    <path d="M0 10H227" stroke="var(--red-line)" stroke-width="1"/>
    <g stroke="var(--orange)" stroke-width=".7" stroke-dasharray="2 1.5">
      <path d="M0 24H227M0 28H227M0 32H227M0 36H227M0 40H227"/>
    </g>
    <text class="axis-label" x="234" y="13">137’24</text>
    <text class="axis-label small" x="236" y="25">137’20</text>
    <text class="axis-label small" x="236" y="30">137’18</text>
    <text class="axis-label small" x="236" y="35">137’16</text>
    <text class="axis-label small" x="236" y="40">137’14</text>
    <text class="axis-label small" x="236" y="45">137’12</text>
    <text class="axis-label" x="234" y="62">137’08</text>
    <use href="#price-candles"/>
    <path d="M211 28H215V32H218L213 37L208 32H211Z" fill="var(--down)"/>
    <polyline fill="none" stroke="var(--osc)" stroke-width="2" stroke-linejoin="round" points="10,172 15,182 30,184 38,172 44,172 52,182 60,186 75,188 80,172 86,170 92,162 100,168 106,160 112,166 120,150 128,150 135,160 145,140 150,142 157,128 163,150 168,160 175,140 180,148 190,140 198,150 212,128 225,128"/>
    <g fill="var(--bar)">
      <rect x="3" y="262" width="3" height="15"/><rect x="10" y="266" width="3" height="11"/>
      <rect x="17" y="260" width="3" height="17"/><rect x="24" y="266" width="3" height="11"/>
      <rect x="31" y="262" width="3" height="15"/><rect x="38" y="268" width="3" height="9"/>
      <rect x="45" y="266" width="3" height="11"/><rect x="52" y="264" width="3" height="13"/>
      <rect x="59" y="258" width="3" height="19"/><rect x="66" y="262" width="3" height="15"/>
      <rect x="73" y="227" width="3" height="50"/><rect x="80" y="254" width="3" height="23"/>
      <rect x="87" y="262" width="3" height="15"/><rect x="94" y="260" width="3" height="17"/>
      <rect x="101" y="266" width="3" height="11"/><rect x="108" y="262" width="3" height="15"/>
      <rect x="115" y="266" width="3" height="11"/><rect x="122" y="264" width="3" height="13"/>
      <rect x="129" y="266" width="3" height="11"/><rect x="136" y="240" width="3" height="37"/>
      <rect x="143" y="258" width="3" height="19"/><rect x="150" y="264" width="3" height="13"/>
      <rect x="157" y="266" width="3" height="11"/><rect x="164" y="264" width="3" height="13"/>
      <rect x="171" y="266" width="3" height="11"/><rect x="178" y="264" width="3" height="13"/>
      <rect x="185" y="266" width="3" height="11"/><rect x="192" y="264" width="3" height="13"/>
      <rect x="199" y="262" width="3" height="15"/><rect x="206" y="264" width="3" height="13"/>
      <rect x="213" y="262" width="3" height="15"/><rect x="220" y="268" width="3" height="9"/>
    </g>
  </svg>

  <div class="chart-heading" style="left:663px">EXIT (BUY)</div>
  <svg class="chart exit" viewBox="0 0 297 297" role="img" aria-label="Exit (buy) chart: price candles, oscillator and volume">
    <use href="#chart-frame"/>
    <path d="M0 10H227" stroke="var(--grid)" stroke-width=".6"/>
    <path d="M0 34H227" stroke="var(--orange)" stroke-width=".8" stroke-dasharray="2 1.5"/>
    <path d="M0 50H227" stroke="var(--navy-dash)" stroke-width=".8" stroke-dasharray="2 1.5"/>
    <text class="axis-label" x="234" y="13">137’24</text>
    <text class="axis-label small" x="236" y="36">137’16</text>
    <text class="axis-label small" x="236" y="52">137’10</text>
    <text class="axis-label" x="234" y="62">137’08</text>
    <use href="#price-candles"/>
    <path d="M198 28H202V32H205L200 37L195 32H198Z" fill="var(--down)"/>
    <polyline fill="none" stroke="var(--osc)" stroke-width="2" stroke-linejoin="round" points="10,172 20,172 28,160 36,168 44,172 52,182 60,186 75,188 80,170 86,170 92,160 100,166 106,154 112,162 120,152 128,150 135,158 145,146 152,146 158,132 165,144 172,150 178,138 185,146 192,140 200,142 212,130 225,142"/>
    <g fill="var(--bar)">
      <rect x="3" y="270" width="3" height="7"/><rect x="10" y="270" width="3" height="7"/>
      <rect x="17" y="268" width="3" height="9"/><rect x="24" y="270" width="3" height="7"/>
      <rect x="31" y="266" width="3" height="11"/><rect x="38" y="268" width="3" height="9"/>
      <rect x="45" y="262" width="3" height="15"/><rect x="52" y="256" width="3" height="21"/>
      <rect x="59" y="244" width="3" height="33"/><rect x="66" y="218" width="3" height="59"/>
      <rect x="73" y="252" width="3" height="25"/><rect x="80" y="226" width="3" height="51"/>
      <rect x="87" y="256" width="3" height="21"/><rect x="94" y="262" width="3" height="15"/>
      <rect x="101" y="256" width="3" height="21"/><rect x="108" y="262" width="3" height="15"/>
      <rect x="115" y="266" width="3" height="11"/><rect x="122" y="264" width="3" height="13"/>
      <rect x="129" y="266" width="3" height="11"/><rect x="136" y="256" width="3" height="21"/>
      <rect x="143" y="256" width="3" height="21"/><rect x="150" y="264" width="3" height="13"/>
      <rect x="157" y="266" width="3" height="11"/><rect x="164" y="264" width="3" height="13"/>
      <rect x="171" y="266" width="3" height="11"/><rect x="178" y="264" width="3" height="13"/>
      <rect x="185" y="266" width="3" height="11"/><rect x="192" y="264" width="3" height="13"/>
      <rect x="199" y="246" width="3" height="31"/><rect x="206" y="250" width="3" height="27"/>
      <rect x="213" y="264" width="3" height="13"/><rect x="220" y="266" width="3" height="11"/>
    </g>
  </svg>
</div>
</body>
</html>
```